Cannabis Company needs a packaging design for a 4x6 pouch

We need a design for a new cannabis company. Included is the logo in red. The logo color can change. Whatever color looks best with the design is what we'll use. The design can't include any cartoon characters or anything that may appeal to children. We have multiple products that are similar that will be using the same design. The pouch will contain 10 pyramid shaped gummies. The look we're going for is modern, simple, but eye catching. I included a handful of photos of packaging we like if that helps.

```html
<!DOCTYPE html>
<html lang="en">
<head>
<meta charset="utf-8">
<title>Verdalo Delta 8 THC Gummies – Orange Pouch</title>
<link href="https://fonts.googleapis.com/css2?family=Bebas+Neue&family=Montserrat:wght@600;700;800&family=Poppins:wght@400;500&display=swap" rel="stylesheet">
<style>
  :root {
    --backdrop: #ececec;
    --pouch: #ffffff;
    --orange: #f57a1c;
    --orange-deep: #e8620e;
    --orange-light: #fb9a3c;
    --maroon: #7a0f0f;
    --icon-bg: #ececec;
    --ink: #3f3f3f;
    --ink-soft: #6b6b6b;
  }
  * { margin: 0; padding: 0; box-sizing: border-box; }
  html, body { width: 1200px; height: 2400px; overflow: hidden; background: var(--backdrop); }
  .pouch-front {
    position: absolute; left: 60px; top: 390px; width: 1080px; height: 1620px;
    background: var(--pouch); box-shadow: 0 6px 24px rgba(0,0,0,.22);
  }
  .flavor-photo {
    position: absolute; left: 241px; top: 0; width: 592px; height: 691px;
    border-radius: 0 0 36px 36px;
    background: radial-gradient(circle at 30% 25%, var(--orange-light), transparent 45%),
                radial-gradient(circle at 75% 70%, var(--orange-light), transparent 40%),
                linear-gradient(160deg, var(--orange) 0%, var(--orange-deep) 100%);
  }
  .brand {
    position: absolute; left: 241px; top: 492px; width: 592px;
    display: flex; align-items: center; justify-content: center; gap: 18px;
  }
  .brand-dot { width: 34px; height: 34px; border-radius: 50%; background: #fff; }
  .brand-name {
    font-family: "Montserrat", sans-serif; font-weight: 700; font-size: 72px;
    color: #fff; letter-spacing: -1px; line-height: 1;
  }
  .headline {
    position: absolute; left: 236px; top: 700px; width: 597px; height: 340px;
    overflow: visible;
  }
  .headline text { font-family: "Bebas Neue", "Oswald", sans-serif; }
  .headline-thc { font-size: 168px; fill: var(--maroon); }
  .headline-thc .accent { fill: var(--orange); }
  .headline-gummies { font-size: 218px; fill: var(--orange); }
  .flavor-band {
    position: absolute; left: 236px; top: 1035px; width: 597px; height: 104px;
    background: var(--maroon); border-radius: 6px;
    display: flex; align-items: center; justify-content: center;
    font-family: "Montserrat", sans-serif; font-weight: 800; font-size: 86px;
    color: #fff; letter-spacing: 26px; padding-left: 26px; white-space: nowrap;
  }
  .claims { position: absolute; left: 0; top: 1198px; width: 1080px; height: 180px; }
  .claim { position: absolute; width: 200px; text-align: center; }
  .claim-icon {
    width: 102px; height: 102px; margin: 0 auto; border-radius: 50%;
    background: var(--icon-bg); display: flex; align-items: center; justify-content: center;
  }
  .claim-label {
    margin-top: 30px; font-family: "Poppins", sans-serif; font-weight: 500;
    font-size: 34px; line-height: 1.02; color: var(--ink); text-transform: uppercase;
  }
  .claim-gluten { left: 215px; }
  .claim-gmo { left: 434px; }
  .claim-fat { left: 655px; }
  .claim-divider {
    position: absolute; top: 0; height: 178px; border-left: 2px dashed var(--orange);
  }
  .count-pill {
    position: absolute; left: 382px; top: 1431px; width: 324px; height: 50px;
    background: var(--orange); border-radius: 8px;
    display: flex; align-items: center; justify-content: center;
    font-family: "Montserrat", sans-serif; font-weight: 700; font-size: 32px;
    color: #fff; letter-spacing: 5px; white-space: nowrap;
  }
  .dose-note {
    position: absolute; left: 0; top: 1494px; width: 1080px; text-align: center;
    font-family: "Poppins", sans-serif; font-weight: 400; font-size: 24px;
    color: var(--ink-soft); letter-spacing: 8px; white-space: nowrap;
  }
</style>
</head>
<body>
  <main class="pouch-front">
    <div class="flavor-photo" role="img" aria-label="Photo of sliced oranges filling the panel"></div>
    <div class="brand">
      <span class="brand-dot"></span>
      <span class="brand-name">verdalo</span>
    </div>

    <svg class="headline" viewBox="0 0 597 340" role="heading" aria-level="1" aria-label="Delta 8 THC Gummies">
      <text class="headline-thc" x="0" y="153" textLength="597" lengthAdjust="spacingAndGlyphs">DELTA <tspan class="accent">8</tspan> THC</text>
      <text class="headline-gummies" x="0" y="321" textLength="597" lengthAdjust="spacingAndGlyphs">GUMMIES</text>
    </svg>
    <div class="flavor-band">ORANGE</div>

    <section class="claims">
      <div class="claim claim-gluten">
        <div class="claim-icon">
          <svg width="62" height="62" viewBox="0 0 62 62" fill="none" stroke="#7a0f0f" stroke-width="2.5">
            <circle cx="31" cy="31" r="27"/>
            <line x1="12" y1="12" x2="50" y2="50"/>
            <path d="M31 14v36M31 22c-6-2-8 2-8 2s2 4 8 2M31 22c6-2 8 2 8 2s-2 4-8 2M31 32c-6-2-8 2-8 2s2 4 8 2M31 32c6-2 8 2 8 2s-2 4-8 2"/>
          </svg>
        </div>
        <p class="claim-label">Gluten<br>Free</p>
      </div>
      <div class="claim-divider" style="left:415px"></div>
      <div class="claim claim-gmo">
        <div class="claim-icon">
          <svg width="62" height="62" viewBox="0 0 62 62" fill="none" stroke="#7a0f0f" stroke-width="2.5">
            <circle cx="31" cy="31" r="27"/>
            <line x1="12" y1="50" x2="50" y2="12"/>
            <text x="31" y="36" text-anchor="middle" font-family="Poppins, sans-serif" font-size="15" fill="#7a0f0f" stroke="none">GMO</text>
          </svg>
        </div>
        <p class="claim-label">Non<br>GMO</p>
      </div>
      <div class="claim-divider" style="left:655px"></div>
      <div class="claim claim-fat">
        <div class="claim-icon">
          <svg width="62" height="62" viewBox="0 0 62 62" fill="none" stroke="#7a0f0f" stroke-width="2.5">
            <circle cx="31" cy="31" r="27"/>
            <line x1="12" y1="12" x2="50" y2="50"/>
            <path d="M26 18c-6 8-9 12-9 17a9 9 0 0 0 18 0c0-5-3-9-9-17z"/>
            <path d="M38 28c-4 5-6 8-6 11a6 6 0 0 0 12 0c0-3-2-6-6-11z"/>
          </svg>
        </div>
        <p class="claim-label">Fat<br>Free</p>
      </div>
    </section>

    <div class="count-pill">10 GUMMIES</div>
    <p class="dose-note">25MG DELTA 10 PER GUMMY</p>
  </main>
</body>
</html>
```